Bramwick Lawn Care

I am looking for a postcard design for a lawn maintenance company. The postcards will be sent EDDM and have a size of 7"x 5" color, both sides. This company is relatively new. It is located in New Jersey, 08007. We maintain peoples properties at a reasonable cost. We pride ourselves in a no contract/ commitment during the season. Some of the work that is done includes: mowing, trimming, edging, application of fertilizers, weed control on the property, aeration of the soil, cutting of small trees, mulching, and hedging. We are fully licensed and insured. I do not approve of "Hurry in while this offer lasts" propaganda. I would like this postcard to be inviting. The phone number (612) 405- 9173, email BramwickLawnCare@fernmail.net, and website (BramwickLawnCare.net) should somehow be incorporated into the design.

Target Market(s)

Targeting people who are looking for lawn maintenance.

Industry/Entity Type

It Company

Requirements
Must have
• Subtle, welcoming design. The design must have phone number, email, and web address. Contracts are not mandatory, so that could be incorporated as well.
Nice to have
• Light, refreshing spring is in the air kind of feel.
Should not have
• Generic design similar to the "mundane"

```html
<!DOCTYPE html>
<html lang="en">
<head>
<meta charset="utf-8">
<title>Bramwick Lawn Care – Postcard</title>
<link rel="stylesheet" href="https://fonts.googleapis.com/css2?family=Anton&family=Tinos&family=Gelasio&display=swap">
<style>
  :root {
    --sky-top: #86a872;
    --sky-mid: #b7bf82;
    --sky-warm: #d9c98d;
    --leaf: #3b7834;
    --leaf-deep: #2f6a2b;
    --ink: #111111;
    --fence: #f4f4ef;
    --grass: #5f9a35;
    --grass-dark: #3f7a22;
    --mower-red: #d8432a;
    --mower-black: #1b1b1b;
  }
  * { box-sizing: border-box; margin: 0; padding: 0; }
  html, body { width: 1200px; height: 465px; overflow: hidden; background: #ffffff; }
  .postcard { position: relative; width: 1200px; height: 465px; display: flex; }
  .side {
    position: relative;
    height: 465px;
    overflow: hidden;
    background:
      radial-gradient(ellipse at 50% 60%, var(--sky-warm) 0%, rgba(217,201,141,0) 60%),
      linear-gradient(180deg, var(--sky-top) 0%, var(--sky-mid) 45%, var(--sky-warm) 75%);
  }
  .side--front { width: 613px; }
  .side--back { width: 587px; }

  .scenery {
    position: absolute; left: 0; right: 0; top: 330px; bottom: 0;
    background: linear-gradient(180deg, rgba(244,244,239,0) 0%, var(--fence) 10%, var(--fence) 45%, var(--grass) 58%, var(--grass-dark) 100%);
  }
  .mower {
    position: absolute;
    background: linear-gradient(135deg, var(--mower-black) 0%, var(--mower-black) 45%, var(--mower-red) 65%, #b8351f 100%);
    border-radius: 36px 36px 22px 22px;
    opacity: .92;
  }
  .side--front .mower { left: 296px; top: 318px; width: 134px; height: 122px; }
  .side--back .mower { left: 250px; top: 318px; width: 300px; height: 122px; }

  .headline-relax {
    position: absolute; left: 298px; top: 2px;
    font-family: "Anton", sans-serif;
    font-weight: 400;
    font-size: 94px; line-height: 1;
    letter-spacing: 15px;
    color: var(--leaf);
  }
  .headline-we-do {
    position: absolute; left: 27px; top: 128px;
    font-family: "Tinos", serif;
    font-weight: 400;
    font-size: 82px; line-height: 1;
    color: var(--ink);
  }
  .promises {
    position: absolute; left: 298px; top: 124px;
    list-style: none;
    font-family: "Tinos", serif;
    font-size: 24px; line-height: 31px;
    color: var(--ink);
  }
  .services {
    position: absolute; left: 15px; top: 220px;
    font-family: "Tinos", serif;
    font-size: 18px; line-height: 24px;
    white-space: nowrap;
    color: var(--leaf);
  }
  .phone-front {
    position: absolute; left: 15px; top: 332px;
    font-family: "Gelasio", serif;
    font-size: 34px; line-height: 1;
    color: var(--leaf-deep);
    z-index: 2;
  }

  .pricing-note {
    position: absolute; left: 152px; top: 63px;
    font-family: "Tinos", serif;
    font-size: 21px; color: var(--ink);
  }
  .website {
    position: absolute; left: 68px; top: 112px;
    font-family: "Gelasio", serif;
    font-size: 39px; color: var(--leaf);
  }
  .email {
    position: absolute; left: 72px; top: 182px;
    font-family: "Tinos", serif;
    font-size: 21px; color: var(--ink);
  }
  .phone-back {
    position: absolute; left: 64px; top: 226px;
    font-family: "Gelasio", serif;
    font-size: 56px; line-height: 1.1;
    color: var(--leaf);
  }
</style>
</head>
<body>
<main class="postcard">
  <section class="side side--front">
    <div class="scenery" role="img" aria-label="White picket fence over a strip of fresh green lawn"></div>
    <div class="mower" role="img" aria-label="Red and black push lawn mower on the grass"></div>
    <h1 class="headline-relax">RELAX</h1>
    <h2 class="headline-we-do">We do</h2>
    <ul class="promises">
      <li>No contract</li>
      <li>No commitment</li>
      <li>Fully licensed &amp; insured</li>
    </ul>
    <p class="services">Mowing, trimming,cutting of small trees,<br>application of fertilizers,aeration of the soil,<br>cutting of small trees, edging, mulching<br>and much more...</p>
    <p class="phone-front">(612) 405- 9173</p>
  </section>

  <section class="side side--back">
    <div class="scenery" role="img" aria-label="White picket fence over a strip of fresh green lawn"></div>
    <div class="mower" role="img" aria-label="Red and black push lawn mower on the grass"></div>
    <p class="pricing-note">For pricing and detail</p>
    <p class="website">BramwickLawnCare.net</p>
    <p class="email">BramwickLawnCare@fernmail.net</p>
    <p class="phone-back">(612) 405- 9173</p>
  </section>
</main>
</body>
</html>
```